Etiketten für Gin
Zielgruppe
Wir sind eine kleine neue Brennerei im bayerischen Oberland und werden unter den Namen „Silver Kite“ und „Silver Kite Lemon“ zwei GIN-Sorten auf den Markt bringen.
Der GIN wird online und vor Ort verkauft und sollte daher eine exklusiv-auffällige Optik haben um die Kunden zu beeindrucken. Zielkunden sind anspruchsvolle Genießer, welche die bayerische Gastlichkeit und Lebenskultur schätzen.
Neu an den beiden Gins ist, dass sie mit Blütenpollen destilliert werden, was auf dem Etikett erscheinen muss.
Aufgabenstellung
Wir suchen zwei sich ähnelnde GIN-Etiketten deren Design ausdrückt, dass es sich um handgemachte und hochwertige GIN handelt, deren Zutat Blütenpollen bisher einzigartig ist.
Statt der oft üblichen Bezeichnung „London Dry Gin“ soll „Halmberg Dry Gin“ und „handcrafted“ auf dem Etikett erscheinen, zusätzlich natürlich die verkehrsüblichen Angaben.
Abgefüllt wird in weißen 500ml Flaschen Typ Vendu mit Korkverschluss von kapselix.com.
Sinnvoll halten wir ein Frontetikett, lassen aber gerne auch andere Vorschläge zu.

```html
<!DOCTYPE html>
<html lang="de">
<head>
<meta charset="utf-8">
<title>Halmberg Dry Gin – Frontetikett</title>
<link rel="stylesheet" href="https://fonts.googleapis.com/css2?family=Lobster&family=Open+Sans:wght@400;700&display=swap">
<style>
  :root {
    --page: #f4f4f4;
    --label: #ffffff;
    --ink: #262626;
    --night: #272625;
    --gold-light: #f3dfb6;
    --gold: #d9a84a;
    --gold-deep: #b7862a;
    --bronze: #8a5a1e;
    --copper: #7a2e22;
    --text-light: #f2f2f2;
  }
  html, body {
    margin: 0;
    padding: 0;
    width: 670px;
    height: 1200px;
    overflow: hidden;
    background: var(--page);
  }
  .label {
    position: absolute;
    left: 0;
    top: 329px;
    width: 670px;
    height: 542px;
    background: var(--label);
    overflow: hidden;
  }
  .mountain-scene {
    position: absolute;
    left: 0;
    top: 170px;
    width: 670px;
    height: 372px;
    background: linear-gradient(180deg,
      rgba(243,223,182,0) 0%,
      var(--gold-light) 14%,
      var(--gold) 34%,
      var(--gold-deep) 44%,
      var(--night) 58%,
      var(--night) 100%);
  }
  .product-title {
    position: absolute;
    left: 206px;
    top: 14px;
    margin: 0;
    font-family: "Lobster", cursive;
    font-weight: 400;
    font-size: 70px;
    line-height: 65px;
    color: var(--ink);
  }
  .product-title span { display: block; }
  .variant {
    position: absolute;
    left: 214px;
    top: 428px;
    margin: 0;
    font-family: "Open Sans", sans-serif;
    font-weight: 700;
    font-size: 19px;
    line-height: 26px;
    letter-spacing: -0.3px;
    background: linear-gradient(90deg, var(--bronze), var(--gold-light) 45%, var(--gold-deep) 80%, var(--copper));
    -webkit-background-clip: text;
    background-clip: text;
    color: transparent;
  }
  .variant span { display: block; }
  .divider-dot {
    position: absolute;
    left: 307px;
    top: 460px;
    width: 4px;
    height: 4px;
    border-radius: 50%;
    background: var(--text-light);
  }
  .details {
    position: absolute;
    left: 325px;
    top: 430px;
    margin: 0;
    font-family: "Open Sans", sans-serif;
    font-size: 15px;
    line-height: 22px;
    color: var(--text-light);
  }
  .details span { display: block; }
  .details .highlight {
    display: inline-block;
    padding: 0 1px;
    background: linear-gradient(90deg, var(--bronze), var(--gold) 40%, var(--gold-deep) 70%, var(--copper));
  }
</style>
</head>
<body>
  <main class="label">
    <div class="mountain-scene" role="img" aria-label="Goldene Bergkette vor dunklem Gebirgsmassiv mit goldenen Sprenkeln"></div>

    <h1 class="product-title">
      <span>Halmberg</span>
      <span>Dry</span>
      <span>Gin</span>
    </h1>

    <p class="variant">
      <span>LEMON</span>
      <span>SILVER</span>
      <span>KITE</span>
    </p>

    <div class="divider-dot"></div>

    <p class="details">
      <span>handcraftet</span>
      <span><span class="highlight">einzigartig mit blütenpollen</span></span>
      <span>500 ml&nbsp;&nbsp;.&nbsp;&nbsp;45% Vol</span>
    </p>
  </main>
</body>
</html>
```